Webdesign für Software Ingenieurbüro
Vielen Dank für das professionelle Design, Umsetzung mit WordPress und rasche Reaktionszeiten. MondscheinKobold geht die Extrameile.
Zielgruppe
English text below
Meine Firma erstellt Software und bietet sämtliche Dienstleistungen rund um die Softwareentwicklung an.
Die Zielgruppe sind Auftraggeber, welche Software-Engineering/Entwicklungsaufträge vergeben.
English
My company creates software and offers all services related to software development.
The target group are those who award software engineering / development contracts.
Aufgabenstellung
Die bestehende Seite www.tarnvok-systems.ch soll neu und modern designed werden. Die Struktur der Seite (Menuunterteilung) kann (muss aber nicht zwingend) übernommen werden.
Das Logo kann, muss aber nicht übernommen werden.
Ev. als OnePage-Seite gestalten.
Responsive-Design ist zwingend, d.h. die Seite muss sowohl auf dem Desktop wie auch auf dem Mobile-Gerät ansprechend aussehen.
Zur Illustration soll auf Fotos verzichtet werden. Aber es können sehr gerne Vektorgrafiken für die Illustration und/oder Icons verwendet werden.
Link auf Social-Media Qorvu muss vorhanden sein.
Der persönliche Kontakt zum Kunden ist mir wichtig, deshalb sollte mein Foto vorhanden sein. Ev. nicht so prominent wie auf der aktuellen Seite.
Die Umsetzung wird mit Wordpress und einem Standard-Theme geschehen. Falls Sie Wordpress kennen, können Sie das Theme angeben, mit welchem sich die Seite umsetzen lässt.
The existing site www.tarnvok-systems.ch is to be redesigned and modernized. The structure of the page (menu subdivision) can (but does not have to be) mandatory.
The logo can, but does not have to be adopted.
Ev. as a OnePage page.
Responsive design is required, the page must look appealing both on the desktop and on the mobile device.
For the illustration, photographs are not desired. But vector graphics can be used for illustration and / or icons.
Link to social media Qorvu must be available.
Personal contact with the customer is important to me, so my photo should be available. Ev. not as prominent as on the current page.
The implementation will be done with Wordpress and a standard theme. If you are familiar with Wordpress, you can specify the theme with which the page can be implemented.

```html
<!DOCTYPE html>
<html lang="de">
<head>
<meta charset="utf-8">
<title>Tarnvok Systems – Softwareentwicklung</title>
<link href="https://fonts.googleapis.com/css2?family=Roboto:ital,wght@0,400;0,700;1,400;1,700;1,900&family=Source+Sans+Pro:wght@400;600&family=Dosis:wght@500;800&display=swap" rel="stylesheet">
<style>
:root{
  --navy:#04142e;
  --navy-mid:#062a52;
  --blue:#0b5d9c;
  --accent:#3a78d8;
  --ink:#3a3a3a;
  --muted:#8a8a8a;
  --line:#444;
  --white:#fff;
  --page:#f4f4f4;
  --dim:rgba(0,0,0,.72);
}
*{box-sizing:border-box;margin:0;padding:0}
html,body{width:841px;height:1200px;overflow:hidden}
body{position:relative;background:var(--page);font-family:"Source Sans Pro",sans-serif;color:var(--ink)}
.abs{position:absolute}
.hero{left:0;top:0;width:841px;height:305px;background:linear-gradient(100deg,var(--navy) 0%,var(--navy-mid) 60%,var(--blue) 100%)}
.brand{left:56px;top:14px;display:flex;align-items:center;gap:6px;color:#d8dde6;font:700 12px/1 "Roboto",sans-serif}
.brand-dot{width:14px;height:14px;border-radius:50%;border:2px solid #c8ced8}
.nav{top:23px;left:494px;display:flex;gap:25px;font-size:8px;color:#c8d2e0}
.nav .active{border-bottom:1px solid #c8d2e0;padding-bottom:3px}
.nav-sep{left:716px;top:24px;width:1px;height:8px;background:#c8d2e0}
.social{display:flex;gap:7px}
.social span{width:11px;height:11px;border:1px solid #c8d2e0}
.hero-title{top:96px;width:841px;text-align:center;font:italic 400 18px "Roboto",sans-serif;color:#e6ebf2}
.hero-title b{font-weight:900}
.hero-text{top:135px;left:250px;width:341px;text-align:center;font-size:8.5px;line-height:11.5px;color:#c8d2e0}
.hero-btn{left:359px;top:185px;width:122px;height:20px;border-radius:10px;background:#2f6fcf;color:#fff;font-size:6.5px;font-weight:600;text-align:center;line-height:20px;letter-spacing:.2px}
.stats{left:158px;top:249px;width:525px;height:81px;background:var(--white);border-radius:3px;display:flex;box-shadow:0 2px 6px rgba(0,0,0,.15)}
.stat{flex:1;text-align:center;padding-top:13px;position:relative}
.stat+.stat::before{content:"";position:absolute;left:0;top:18px;height:45px;border-left:1px solid var(--navy-mid)}
.stat-num{font:800 33px/1 "Dosis",sans-serif;color:var(--navy-mid)}
.stat-label{font-size:13px;color:#333;margin-top:3px}
.tech{left:165px;top:640px;width:512px;height:278px;background:var(--white)}
.tech-title{top:710px;width:841px;text-align:center;font:italic 400 18px/17px "Roboto",sans-serif;color:#222}
.tech-title b{font-weight:900}
.rule{width:32px;height:1px;background:#222;left:404px}
.tech-text{top:792px;left:290px;width:270px;text-align:center;font-size:8.5px;line-height:11px;color:#555}
.logos{left:230px;top:843px;width:380px;display:grid;grid-template-columns:repeat(4,1fr);row-gap:14px;text-align:center;font:600 10px "Source Sans Pro",sans-serif;color:#555}
.dot-l{left:184px;top:834px;width:7px;height:7px;border:1px solid #999}
.dot-r{left:653px;top:834px;width:6px;height:6px;border-radius:50%;background:#555}
.footer{left:0;top:918px;width:841px;height:260px;background:linear-gradient(180deg,var(--navy-mid),var(--navy))}
.footer-title{top:948px;width:841px;text-align:center;font:italic 400 18px "Roboto",sans-serif;color:#dfe6f0}
.footer-title b{font-weight:900}
.footer-text{left:225px;top:1006px;width:165px;font-size:7.5px;line-height:10.5px;color:#c8d2e0}
.footer-text p+p{margin-top:7px}
.profile{left:226px;top:1094px;font:italic 400 8px "Roboto",sans-serif;color:#c8d2e0}
.profile b{font-weight:700}
.f-social{left:226px;top:1116px}
.field{position:absolute}
.field .val{font-size:8px;height:11px;color:#333}
.field .ln{border-bottom:1px solid var(--line);}
.field .lbl{font-size:5px;color:var(--muted);margin-top:3px;letter-spacing:.1px}
.dark .val{color:#dfe6f0}.dark .ln{border-color:#8fa0b8}.dark .lbl{color:#8fa0b8}
.f-btn{left:479px;top:1112px;width:113px;height:19px;border-radius:10px;background:#2f6fcf;color:#fff;font-size:6.5px;font-weight:600;text-align:center;line-height:19px}
.copy{left:0;top:1178px;width:841px;height:22px;background:#020c1c;color:#9aa6b8;font-size:5.5px;text-align:center;line-height:16px}
.overlay{left:0;top:0;width:841px;height:1200px;background:var(--dim)}
.modal{left:164px;top:360px;width:513px;height:338px;background:var(--white)}
.close{right:20px;top:14px}
.m-title{left:132px;top:52px;font:italic 400 18px/21px "Roboto",sans-serif;color:#333}
.m-title b{font-weight:700}
.m-field .ln.focus{border-color:var(--accent)}
.m-field .lbl.focus{color:var(--accent)}
.captcha{left:344px;top:160px;width:38px;height:11px;border:1px dashed #777;background:repeating-linear-gradient(90deg,#eee 0 2px,#bbb 2px 3px);font:700 8px/10px monospace;text-align:center;color:#000}
.attach{right:132px;top:232px;font-size:5.5px;color:var(--accent);display:flex;gap:5px;align-items:center}
.m-btn{left:223px;top:261px;width:67px;height:20px;border-radius:10px;background:linear-gradient(90deg,#2f6fcf,#4b8ae6);color:#fff;font:500 7px/20px "Roboto",sans-serif;text-align:center;box-shadow:0 3px 6px rgba(47,111,207,.4)}
</style>
</head>
<body>
<header class="abs hero"></header>
<div class="abs brand"><span class="brand-dot"></span>Tarnvok Systems</div>
<nav class="abs nav"><span class="active">Home</span><span>Dienstleistungen</span><span>Firma</span><span>Kontakt</span></nav>
<div class="abs nav-sep"></div>
<div class="abs social" style="left:738px;top:23px" aria-label="Verbundo, Qorvu, Velunet"><span></span><span></span><span></span></div>
<h1 class="abs hero-title">Professionelle <b>Softwareentwicklung</b></h1>
<p class="abs hero-text">Tarnvok Systems stellt unter Verwendung modernster Technologien und leichtgewichtiger Prozessen qualitativ hochstehende Software her.</p>
<div class="abs hero-btn">HABEN SIE EIN PROJEKT?</div>
<section class="abs stats">
  <div class="stat"><div class="stat-num">18</div><div class="stat-label">Jahre Erfahrung</div></div>
  <div class="stat"><div class="stat-num">232</div><div class="stat-label">zufriedene Kunden</div></div>
  <div class="stat"><div class="stat-num">15</div><div class="stat-label">Coaching-Projekte</div></div>
</section>
<section class="abs tech"></section>
<h2 class="abs tech-title"><b>Konzentrieren</b> Sie sich<br>auf <b>Technologie</b></h2>
<div class="abs rule" style="top:772px"></div>
<p class="abs tech-text">Über 18 Jahre Erfahrung in der Softwareentwicklung und Entwicklung von Backendsystemen mit hohem Transaktionsaufkommen</p>
<div class="abs dot-l"></div><div class="abs dot-r"></div>
<div class="abs logos"><span>Kavera</span><span>Tabula Store</span><span>Sprossa</span><span>Winkelform</span><span>Orvane</span><span>&lt;xml /&gt;</span><span>Schlafwerk</span><span>Seifkit</span></div>
<footer class="abs footer"></footer>
<h2 class="abs footer-title">Sie können eine <b>Frage stellen</b></h2>
<div class="abs rule" style="top:990px;background:#6d7e96"></div>
<div class="abs footer-text"><p>Tarnvok Systems GmbH fokussiert sich auf die professionelle Softwareentwicklung .</p><p>Ich freue mich auf Ihre Nachricht. Füllen Sie bitte untenstehendes Formular aus. Ich werde so rasch wie möglich mit Ihnen in Kontakt treten.</p></div>
<div class="abs profile">Besuchen Sie mein Profil: &nbsp;<b>Bernhard Kolmer</b></div>
<div class="abs social f-social"><span></span><span></span><span></span></div>
<div class="field dark" style="left:455px;top:1011px;width:161px"><div class="val ln">Alex|</div><div class="lbl">NAME</div></div>
<div class="field dark" style="left:455px;top:1041px;width:161px"><div class="val ln"></div><div class="lbl">E-MAIL</div></div>
<div class="field dark" style="left:455px;top:1071px;width:161px"><div class="val ln"></div><div class="lbl">NACHRICHT</div></div>
<div class="abs f-btn">SCHICKEN NACHRICHT</div>
<div class="abs copy">© Copyright 2010 - 2017 Tarnvok Systems GmbH. All rights reserved.</div>
<div class="abs overlay"></div>
<div class="abs modal" role="dialog" aria-label="Projektanfrage">
  <svg class="abs close" width="14" height="14" viewBox="0 0 14 14"><path d="M1 1L13 13M13 1L1 13" stroke="#222" stroke-width="1"/></svg>
  <h2 class="abs m-title">Wollen Sie die <b>Zusammenarbeit</b><br>beginnen?</h2>
  <div class="field m-field" style="left:132px;top:130px;width:119px"><div class="val ln focus">Alex|</div><div class="lbl focus">NAME</div></div>
  <div class="field m-field" style="left:263px;top:130px;width:119px"><div class="val ln"></div><div class="lbl">WEB SITE</div></div>
  <div class="field m-field" style="left:132px;top:160px;width:119px"><div class="val ln"></div><div class="lbl">E-MAIL</div></div>
  <div class="field m-field" style="left:263px;top:160px;width:60px"><div class="val ln"></div><div class="lbl">COPY CAPTCHA CODE:</div></div>
  <div class="abs captcha">MJ3LM</div>
  <div class="field m-field" style="left:132px;top:190px;width:249px"><div class="val ln"></div><div class="lbl">PROJEKTBESCHREIBUNG</div></div>
  <div class="abs attach"><svg width="6" height="8" viewBox="0 0 6 8"><path d="M4.5 2.5L2 6a1 1 0 0 1-1.5-1L3.5 1a1.3 1.3 0 0 1 2 1.5L3 6" fill="none" stroke="#3a78d8" stroke-width=".7"/></svg>DATEI ANHÄNGEN</div>
  <div class="abs m-btn">SCHICKEN</div>
</div>
</body>
</html>
```